Need to make a KMB water label for my water bottle and packaging. Attached is our Trademarked LOGO for KMB we have a natural spring water that flows through our land that is naturally filtered through pure limestone. want to make a badass label that has our logo in it with our colors

Target Market(s)

Commercial Bottle water

Colors
3176b5

```html
<!DOCTYPE html>
<html lang="en">
<head>
<meta charset="UTF-8">
<title>KMB Natural Spring Water Label</title>
<link rel="stylesheet" href="https://fonts.googleapis.com/css2?family=Arimo:wght@400;700&family=Roboto+Condensed:ital,wght@1,800&display=swap">
<style>
  :root {
    --brand-blue: #3176b5;
    --navy: #1c2a4a;
    --ink: #111111;
    --silver-light: #f4f4f4;
    --silver-mid: #d8d8d8;
    --silver-dark: #bdbdbd;
    --panel-white: #fbfbfb;
    --art-orange: #e9a66a;
    --art-gold: #f1d29a;
    --art-blue: #9dbbd9;
  }
  html, body {
    margin: 0;
    padding: 0;
    width: 1200px;
    height: 325px;
    overflow: hidden;
    background: #ffffff;
  }
  .label {
    position: relative;
    width: 1200px;
    height: 325px;
    overflow: hidden;
    background: linear-gradient(90deg, var(--silver-mid) 0%, var(--silver-light) 16%, var(--silver-mid) 38%, var(--silver-light) 58%, var(--silver-dark) 82%, var(--silver-light) 100%);
    font-family: "Arimo", Arial, sans-serif;
    color: var(--ink);
  }
  .product-story {
    position: absolute;
    left: 14px;
    top: 16px;
    width: 252px;
    text-align: center;
    font-size: 15.5px;
    line-height: 19.6px;
  }
  .product-story h2 {
    margin: 0 0 2px;
    font-size: 16px;
    font-weight: 700;
  }
  .product-story p { margin: 0; }
  .artwork-area {
    position: absolute;
    left: 272px;
    top: 8px;
    width: 696px;
    height: 262px;
    background: linear-gradient(90deg, var(--art-blue) 0%, var(--art-orange) 30%, var(--art-gold) 50%, var(--art-orange) 70%, var(--art-blue) 100%);
    opacity: 0.55;
  }
  .brand-name {
    position: absolute;
    left: 470px;
    top: 80px;
    width: 300px;
    height: 100px;
    display: flex;
    align-items: center;
    justify-content: center;
    font-family: "Arimo", Arial, sans-serif;
    font-weight: 700;
    font-size: 84px;
    letter-spacing: 3px;
    color: var(--brand-blue);
  }
  .info-panel {
    position: absolute;
    left: 975px;
    top: 0;
    width: 100px;
    height: 325px;
    background: var(--panel-white);
  }
  .volume {
    position: absolute;
    left: 972px;
    top: 258px;
    width: 112px;
    text-align: center;
    font-size: 14px;
    line-height: 19px;
    white-space: nowrap;
  }
  .vertical-text {
    position: absolute;
    white-space: nowrap;
    font-size: 14.5px;
    line-height: 18px;
    transform-origin: left bottom;
    transform: rotate(-90deg);
  }
  .upc {
    left: 1028px;
    top: 140px;
  }
  .distributor {
    left: 1112px;
    top: 194px;
    text-align: center;
  }
  .quality-contact {
    left: 1150px;
    top: 194px;
    text-align: left;
  }
  .tagline {
    position: absolute;
    left: 280px;
    width: 700px;
    top: 296px;
    text-align: center;
    white-space: nowrap;
    font-family: "Roboto Condensed", "Arial Narrow", sans-serif;
    font-style: italic;
    font-weight: 800;
    font-size: 20px;
    letter-spacing: 0.2px;
    color: var(--navy);
  }
</style>
</head>
<body>
  <div class="label">
    <section class="product-story">
      <h2>Product Story Here</h2>
      <p>Product story here, product story here, product story here. Product story here, product story here, product story here. Product story here, product story here, product story here, product story here. Product story here, product story here, product story here.</p>
    </section>

    <div class="artwork-area" role="img" aria-label="Area for the colourful water splash artwork behind the brand name"></div>

    <div class="brand-name">KMB</div>

    <div class="info-panel"></div>

    <div class="volume">16.9 FL OZ<br>(1.05 PT) 500ml</div>

    <div class="vertical-text upc">UPC CODE HERE</div>

    <div class="vertical-text distributor">DISTRIBUTED BY ABCDEFGHIJ<br>SOMEWHERE USA</div>

    <div class="vertical-text quality-contact">FOR WATER QUALITY<br>CONTACT 123-123-1234</div>

    <div class="tagline">NATURAL SPRING WATER-NATURALLY FILTERED THROUGH PURE LIMESTONE</div>
  </div>
</body>
</html>
```